" A Limpinho Já é especializada em higienização e impermeabilização de estofados, tanto residenciais quanto automotivos. Também oferecemos serviços de lavanderia para itens como cortinas, edredons, toalhas e peças delicadas. Atendemos com praticidade e comodidade, oferecendo serviço a domicílio e sistema de delivery, sempre priorizando qualidade, cuidado e eficiência em cada atendimento. "

```html
<!DOCTYPE html>
<html lang="pt-BR">
<head>
<meta charset="utf-8">
<title>Cartão de Visita — Limpinho Já</title>
<link href="https://fonts.googleapis.com/css2?family=Nunito:wght@600;700;800;900&display=swap" rel="stylesheet">
<style>
  :root {
    --navy: #0f4a86;
    --navy-dark: #0b3a6b;
    --green: #3cc24a;
    --board: #dfe1e4;
    --board-light: #ebedef;
    --white: #ffffff;
    --text: #1d3f6b;
  }
  * { box-sizing: border-box; margin: 0; padding: 0; }
  html, body { width: 1200px; height: 1200px; overflow: hidden; }
  body {
    font-family: "Nunito", sans-serif;
    background: var(--board);
    position: relative;
  }
  .board-diagonal {
    position: absolute; inset: 0;
    background: linear-gradient(135deg, transparent 0 52%, var(--board-light) 52% 100%);
  }
  .board-diagonal-top {
    position: absolute; inset: 0;
    background: linear-gradient(225deg, var(--board-light) 0 30%, transparent 30% 100%);
    opacity: .6;
  }
  .title-pill {
    position: absolute; left: 372px; top: 41px;
    width: 456px; height: 72px; border-radius: 36px;
    background: var(--navy-dark); color: var(--white);
    display: flex; align-items: center; justify-content: center;
    font-weight: 800; font-size: 34px; letter-spacing: 3px;
  }
  .card {
    position: absolute; left: 247px; width: 706px;
    box-shadow: 0 14px 22px rgba(0,0,0,.18);
    overflow: hidden;
  }
  .card-front { top: 221px; height: 391px; background: var(--navy); }
  .front-deco {
    position: absolute; left: -30px; top: 20px;
    width: 330px; height: 330px; border-radius: 24px;
    background: rgba(255,255,255,.05);
  }
  .front-brand {
    position: absolute; left: 0; right: 0; top: 92px;
    display: flex; flex-direction: column; align-items: center; gap: 14px;
  }
  .brand-dot { width: 92px; height: 92px; border-radius: 50%; background: var(--green); }
  .front-brand .brand-name { color: var(--white); font-weight: 900; font-size: 78px; line-height: 1; }

  .card-back { top: 677px; height: 451px; background: var(--white); }
  .holder {
    position: absolute; left: 0; right: 0; top: 78px; text-align: center;
    color: var(--text); font-size: 27px; font-weight: 600;
  }
  .holder strong { font-weight: 800; }
  .back-brand {
    position: absolute; left: 50px; top: 175px; width: 270px;
    display: flex; flex-direction: column; align-items: center; gap: 12px;
  }
  .back-brand .brand-dot { width: 64px; height: 64px; }
  .back-brand .brand-name { color: var(--navy); font-weight: 900; font-size: 44px; line-height: 1; }
  .contacts {
    position: absolute; left: 324px; top: 140px;
    list-style: none; display: flex; flex-direction: column; gap: 14px;
  }
  .contact { display: flex; align-items: center; gap: 12px; color: var(--text); font-size: 19px; font-weight: 600; line-height: 1.1; }
  .contact svg { width: 28px; height: 28px; flex: none; }
  .bands { position: absolute; left: 0; right: 0; bottom: 0; height: 34px; }
  .band-navy { position: absolute; left: 78px; width: 360px; top: 12px; height: 40px; border-radius: 20px 20px 0 0; background: var(--navy); }
  .band-green { position: absolute; left: 410px; width: 250px; top: 12px; height: 40px; border-radius: 20px 20px 0 0; background: var(--green); }
</style>
</head>
<body>
  <div class="board-diagonal"></div>
  <div class="board-diagonal-top"></div>

  <div class="title-pill">CARTÃO DE VISITA</div>

  <section class="card card-front">
    <div class="front-deco"></div>
    <div class="front-brand">
      <span class="brand-dot"></span>
      <span class="brand-name">Limpinho Já</span>
    </div>
  </section>

  <section class="card card-back">
    <p class="holder"><strong>Nome e Sobrenome</strong> - Diretor Comercial</p>

    <div class="back-brand">
      <span class="brand-dot"></span>
      <span class="brand-name">Limpinho Já</span>
    </div>

    <ul class="contacts">
      <li class="contact">
        <svg viewBox="0 0 28 28"><circle cx="14" cy="14" r="14" fill="#3cc24a"/><rect x="10" y="7" width="8" height="14" rx="1.5" fill="none" stroke="#fff" stroke-width="2"/><circle cx="14" cy="18" r="1" fill="#fff"/></svg>
        <span>(71) 90410-5821 | (71)90388-7360</span>
      </li>
      <li class="contact">
        <svg viewBox="0 0 28 28"><circle cx="14" cy="14" r="14" fill="#0f4a86"/><rect x="7" y="9" width="14" height="10" rx="1" fill="#fff"/><path d="M7 9.5 L14 15 L21 9.5" fill="none" stroke="#0f4a86" stroke-width="1.5"/></svg>
        <span>contato@limpinhoja.com.br</span>
      </li>
      <li class="contact">
        <svg viewBox="0 0 28 28"><circle cx="14" cy="14" r="14" fill="#3cc24a"/><path d="M14 6 a5.5 5.5 0 0 1 5.5 5.5 c0 4 -5.5 10 -5.5 10 s-5.5 -6 -5.5 -10 A5.5 5.5 0 0 1 14 6z" fill="#fff"/><circle cx="14" cy="11.5" r="2" fill="#3cc24a"/></svg>
        <span>Rua das Acácias, 210<br>Cidade/UF - CEP: 40000-000</span>
      </li>
      <li class="contact">
        <svg viewBox="0 0 28 28"><circle cx="14" cy="14" r="14" fill="#0f4a86"/></svg>
        <span>@limpinhoja</span>
      </li>
    </ul>

    <div class="bands">
      <div class="band-navy"></div>
      <div class="band-green"></div>
    </div>
  </section>
</body>
</html>
```